Project Management Consultancy needs logo, business card and stationary design

I need a logo, business card and stationary design for a start-up project management consultancy servicing clients in corporate, education, aviation, local government and construction sectors.

The business will provide professional advice to clients and our people, knowledge and experience is essentially what we sell.

Our role is to assist our clients in delivering successful construction and transition projects whilst ensuring that their needs are identified, understood and achieved.

The company is small and provides a tailor made service for our clients. We pride ourselves on being
- professional
- innovative
- collaborative
- dependable
- communicative
- confident
- bold
The logo, business card and stationary should reflect this.

Can you please include the following on the stationary as appropriate.
Address:
27 Melverton Crescent
Coledale
NSW 2748

ABN: 42 873 306 129

I very much look forward to receiving your designs.

Greg T.

Target Market(s)

Corporate clients such as: airports, universities, government, financial organisations, etc.

Industry/Entity Type

Management Consulting

Contact Information for Business Card

Greg Tolliver
Director
Tolliver Management Consulting Pty Ltd
e. greg.tolliver@tolliver-mc.com.au
m. +61 438 590 163

Font styles to use
Other font styles liked:
• perhaps Arial Narrow? I am open to suggestions

Requirements
Must have
• An dynamic and corporate look and feel.
Should not have
• Should not be boring.

```html
<!DOCTYPE html>
<html lang="en">
<head>
<meta charset="utf-8">
<title>Tolliver Management Consulting — Letterhead</title>
<link href="https://fonts.googleapis.com/css2?family=Jost:wght@400;500&family=Source+Sans+3:wght@400;600;700&display=swap" rel="stylesheet">
<style>
  :root {
    --ink: #111111;
    --paper: #ffffff;
    --frame: #333333;
  }
  html, body {
    margin: 0;
    padding: 0;
    width: 894px;
    height: 1200px;
    overflow: hidden;
    background: var(--paper);
  }
  .canvas {
    position: relative;
    width: 894px;
    height: 1200px;
    background: var(--paper);
    color: var(--ink);
  }
  .sheet {
    position: absolute;
    left: 75px;
    top: 72px;
    width: 745px;
    height: 1052px;
    border: 1px solid var(--frame);
    box-sizing: border-box;
  }
  .brand {
    position: absolute;
    left: 0;
    right: 0;
    top: 120px;
    text-align: center;
  }
  .brand-mark {
    display: block;
    margin: 0 auto;
  }
  .brand-name {
    margin: 8px 0 0;
    font-family: "Jost", sans-serif;
    font-weight: 400;
    font-size: 26px;
    letter-spacing: 0.16em;
    padding-left: 0.16em;
    line-height: 1;
  }
  .brand-tagline {
    margin: 7px 0 0;
    font-family: "Source Sans 3", sans-serif;
    font-weight: 700;
    font-size: 7.5px;
    letter-spacing: 0.2em;
    padding-left: 0.2em;
    line-height: 1;
  }
  .signatory {
    position: absolute;
    left: 0;
    right: 0;
    top: 1004px;
    text-align: center;
  }
  .signatory-name {
    margin: 0;
    font-family: "Jost", sans-serif;
    font-weight: 400;
    font-size: 18px;
    letter-spacing: 0.1em;
    padding-left: 0.1em;
    line-height: 1;
  }
  .signatory-role {
    margin: 4px 0 0;
    font-family: "Source Sans 3", sans-serif;
    font-weight: 600;
    font-size: 10.5px;
    letter-spacing: 0.06em;
    line-height: 1;
  }
  .rule {
    position: absolute;
    left: 146px;
    top: 1043px;
    width: 601px;
    height: 2px;
    background: var(--ink);
  }
  .contact {
    position: absolute;
    left: 0;
    right: 0;
    top: 1052px;
    text-align: center;
    font-family: "Source Sans 3", sans-serif;
    font-size: 9.8px;
    line-height: 14px;
  }
  .contact p { margin: 0; }
  .contact b { font-weight: 700; }
</style>
</head>
<body>
<div class="canvas">
  <div class="sheet" aria-hidden="true"></div>

  <header class="brand">
    <svg class="brand-mark" width="90" height="90" viewBox="0 0 90 90" aria-hidden="true">
      <circle cx="45" cy="45" r="42" fill="none" stroke="var(--ink)" stroke-width="4"/>
    </svg>
    <h1 class="brand-name">TOLLIVER</h1>
    <p class="brand-tagline">MANAGEMENT CONSULTING</p>
  </header>

  <footer>
    <div class="signatory">
      <p class="signatory-name">GREG TOLLIVER</p>
      <p class="signatory-role">DIRECTOR</p>
    </div>
    <div class="rule"></div>
    <div class="contact">
      <p>Tolliver Management Consulting Pty Ltd &nbsp;|&nbsp; ABN: 42 873 306 129</p>
      <p><b>e.</b> greg.tolliver@tolliver-mc.com.au &nbsp;|&nbsp; <b>m.</b> +61 438 590 163 &nbsp;|&nbsp; 27 Melverton Crescent, Brackenvale QLD 2748</p>
    </div>
  </footer>
</div>
</body>
</html>
```